Fernhold Capital - Web Design

I have recently established a business called Fernhold Capital. The business is focused on providing property developers with project financing solutions. This is not a real estate website so please do not provide such pics or design. I provide financial solutions.

I have been in the financial markets for the past 20 years covering all asset classes from trading through to portfolio management, structuring and business development. The majority of this time was spent with building new business and expanding into new opportunities.

This is a start-up business so there isn't much content at this stage. Therefore, its all about first impressions. I want a design that portray confidence; and that I can deliver a workable solution. It must provide the perception of sophistication, innovation, yet simplistic so its not trying to deceive/hide something. Most importantly it must give the Client a sense of trust and reliability.

I would like to have the website portray my depth of experience in providing financing solutions and consultancy services in achieving the investment objectives. However, I would like to avoid looking like a one man band. I do have access to resources just not directly employed by the company.

Anyway, I hope this is enough to at least wet your appetite. I recently had a logo created on PixelGuild that should set the theme/style of the website

Project Deadline Extended
Reason: Increase time to allow web designer/developer more time to understand the style I am after.

All, Thank you for your current designs. I am based in Singapore, however, I am currently traveling today but will respond by later tonight or tomorrow. Owen

All, A general observation. Please do not include photos of houses, architectural drawings or images that portal construction or real estate. This implies I am either a property agent or in some way directly involve in selling property...very misleading. Remember, I am involved in provide financial solutions not selling property. Owen

All, Please avoid using numerous people within the site as it may represent that my business has a large number of staff when in fact its only me. However, I also don't want to look like a "one man band". So be balanced on using people - I am not sure I want people at all. Thanks Owen

Some designers are not reading the brief or previous messages. If you do more then once I will simply not comment and eliminate ask not to provide any more.

please stop using pictures and/or logos that imply - I manage their money - I protect their money - I grow their money - I offer homes loans - that I do house calls with individuals (i.e no couples shaking heads with a guy) - no house pictures or symbols i.e. it looks like a property website - I have a large organisation (i.e. team of people) If any design include the above I will eliminate it REMEMBER: I am providing innovative financial solutions - NOT asset/fund manager, bank manager or real estate manager thank you

All Please be creative and innovative with your pics. Also ensure you have the rights to use the pics. I have seen basic stock photos being used and again have not read by brief or previous comments. For instance, they use the words "sustainable growth" in google and click on images and you will see most of the images being used. these will be eliminated instantly and not asked to return.

Please, if you use the name of the Company as a Label or Statement can please ensure it remains in the same style as the Logo, i.e. all Caps Large with small.

All, I have decided that I don't want to have people in the main pic on the front page so please provide other inspirational pics. Thanks

guys I found a coffee advert whilst in Vietnam. I like the colour selection and thought it would be inspirational.i ahve added it yo my bried f

Real Estate

Coded - Design and coding required

```html
<!DOCTYPE html>
<html lang="en">
<head>
<meta charset="utf-8">
<title>Fernhold Capital</title>
<link href="https://fonts.googleapis.com/css2?family=Open+Sans:ital,wght@0,400;0,600;0,700;1,400&family=Cinzel:wght@600&display=swap" rel="stylesheet">
<style>
:root{
  --black:#050505;
  --footer:#0a0a0a;
  --bar:#111;
  --gold:#b58a22;
  --gold-light:#d4a53a;
  --navy:#0c2a40;
  --navy-text:#102e48;
  --grey:#555;
  --line:#e3e3e3;
}
*{margin:0;padding:0;box-sizing:border-box}
html,body{width:864px;height:1200px;overflow:hidden}
body{position:relative;background:#fff;font-family:"Open Sans",Arial,sans-serif;color:var(--grey)}
.abs{position:absolute}
.header{left:0;top:0;width:864px;height:54px;background:var(--black)}
.brand{left:72px;top:10px;display:flex;align-items:center;gap:8px}
.brand-mark{width:30px;height:30px;border-radius:50%;background:var(--gold)}
.brand-name{font-family:"Cinzel",serif;color:var(--gold);font-size:15px;letter-spacing:2px;line-height:1}
.brand-name small{display:block;font-size:6px;letter-spacing:5px;margin-top:3px;padding-left:16px}
.tagline{left:341px;top:21px;color:#fff;font-style:italic;font-size:9.3px}
.nav{left:0;top:54px;width:864px;height:32px;background:linear-gradient(#141414,#050505);border-top:1px solid #1c1c1c}
.nav a{position:absolute;top:0;height:32px;line-height:32px;color:#fff;font-size:7.6px;font-weight:700;text-decoration:none;text-transform:uppercase}
.nav a.active{left:72px;width:81px;text-align:center;background:linear-gradient(#c8992c,#8a6514)}
.hero{left:0;top:86px;width:864px;height:291px;background:radial-gradient(ellipse at 25% 30%,#8a6a2c 0%,#3b3522 25%,#152238 55%,#0a1426 100%)}
.hero-title{left:540px;top:178px;color:var(--gold-light);font-size:20px;font-weight:600;letter-spacing:.5px}
.hero-text{left:542px;top:210px;color:#fff;font-size:9.4px;line-height:18.5px;text-transform:uppercase}
.hero-arrows{left:795px;top:258px;display:flex;gap:2px}
.hero-arrows span{width:18px;height:17px;background:rgba(255,255,255,.12);display:flex;align-items:center;justify-content:center}
.welcome{left:0;top:377px;width:864px;height:128px;background:var(--navy);text-align:center;color:#fff}
.welcome h1{margin-top:21px;color:var(--gold-light);font-size:14.5px;font-weight:600}
.welcome p{font-size:10.6px;line-height:21px;margin:0 auto;width:700px}
.feature{top:537px;width:230px}
.feature .icon{position:absolute;left:0;top:0;width:39px;height:39px;border-radius:50%;background:var(--navy);display:flex;align-items:center;justify-content:center}
.feature .icon.gold{background:var(--gold)}
.feature h3{margin-left:53px;color:var(--navy-text);font-size:9.8px;font-weight:400;margin-top:3px}
.feature p{margin-left:53px;font-size:7.5px;line-height:16px;margin-top:3px;color:#444}
.what{left:0;top:632px;width:864px;text-align:center}
.what h2{color:var(--navy-text);font-size:14px;font-weight:700}
.what p{font-size:8.6px;margin-top:9px;color:#444}
.service{top:697px;width:170px}
.service .photo{height:118px}
.service h4{margin-top:14px;color:var(--navy-text);font-size:8.2px;font-weight:700;text-transform:uppercase;margin-left:-1px}
.service p{font-size:7.6px;line-height:17px;margin-top:5px;color:#444}
.partners{left:0;top:904px;width:864px;height:84px;border-top:1px solid var(--line)}
.partner{position:absolute;top:38px;font-size:12px;font-weight:700;color:#333;display:flex;align-items:center;gap:5px}
.partner i{width:11px;height:11px;background:#333;display:inline-block}
.footer{left:0;top:988px;width:864px;height:176px;background:var(--footer);font-family:Arial,sans-serif}
.col{position:absolute;top:30px}
.col h5{color:#fff;font-family:"Open Sans",Arial,sans-serif;font-size:8.4px;font-weight:700;text-transform:uppercase;margin-bottom:11px}
.col p{color:#888;font-size:7.2px;line-height:16.8px}
.col a{display:block;color:#888;font-size:7.2px;line-height:16px;text-decoration:none}
.social{display:flex;align-items:center;gap:6px;color:#888;font-size:7.2px;margin-bottom:8px}
.social span{width:17px;height:17px;border:1px solid #444}
.bottom{left:0;top:1164px;width:864px;height:36px;background:var(--bar);color:#888;font-family:Arial,sans-serif;font-size:7.2px;text-align:center;line-height:36px}
</style>
</head>
<body>
<header class="abs header">
  <div class="abs brand"><span class="brand-mark"></span><div class="brand-name">FERNHOLD<small>CAPITAL</small></div></div>
  <p class="abs tagline">THE BUSINESS IS FOCUSED ON PROVIDING PROPERTY DEVELOPERS WITH PROJECT FINANCING SOLUTIONS.</p>
</header>
<nav class="abs nav">
  <a class="active" href="#">Home</a>
  <a href="#" style="left:176px">About Us</a>
  <a href="#" style="left:266px">Services</a>
  <a href="#" style="left:351px">Solutions</a>
  <a href="#" style="left:446px">Carriers</a>
  <a href="#" style="left:533px">Clients</a>
  <a href="#" style="left:614px">Testimonials</a>
  <a href="#" style="left:720px">Contact Us</a>
</nav>
<section class="abs hero" role="img" aria-label="Night view of a lit steel arch bridge over a harbour with a city skyline"></section>
<h2 class="abs hero-title">FERNHOLD CAPITAL</h2>
<p class="abs hero-text">The business is focused on providing property developers<br>with project financing solutions</p>
<div class="abs hero-arrows">
  <span><svg width="6" height="8" viewBox="0 0 6 8"><path d="M5 0 1 4l4 4" fill="none" stroke="#888"/></svg></span>
  <span><svg width="6" height="8" viewBox="0 0 6 8"><path d="M1 0l4 4-4 4" fill="none" stroke="#888"/></svg></span>
</div>
<section class="abs welcome">
  <h1>WELCOME TO FERNHOLD CAPITAL</h1>
  <p>The business is focused on providing property developers with project financing solutions.</p>
  <p>We are in the financial markets for the past 20 years covering all asset classes from trading through to portfolio management, structuring and business development.</p>
</section>
<div class="abs feature" style="left:72px">
  <div class="icon gold"><svg width="18" height="14" viewBox="0 0 18 14"><path d="M1 1v12h16M3 10l4-4 3 3 6-6" fill="none" stroke="#fff" stroke-width="1.6"/></svg></div>
  <h3>Es simplemente el texto de</h3>
  <p>Lorem Ipsum is simply dummy text of the printing and typesetting industry. deen the industry's...</p>
</div>
<div class="abs feature" style="left:325px">
  <div class="icon"><svg width="18" height="14" viewBox="0 0 18 14" fill="#fff"><circle cx="9" cy="4" r="3"/><circle cx="3.5" cy="5" r="2.2"/><circle cx="14.5" cy="5" r="2.2"/><rect x="4" y="8" width="10" height="6" rx="3"/><rect x="0" y="8.5" width="5" height="4.5" rx="2"/><rect x="13" y="8.5" width="5" height="4.5" rx="2"/></svg></div>
  <h3>Es simplemente el texto de</h3>
  <p>Lorem Ipsum is simply dummy text of the printing and typesetting industry. deen the industry's...</p>
</div>
<div class="abs feature" style="left:579px">
  <div class="icon"><svg width="18" height="16" viewBox="0 0 18 16"><circle cx="6" cy="9" r="3.5" fill="none" stroke="#fff" stroke-width="2.4" stroke-dasharray="2 1.2"/><circle cx="13" cy="4.5" r="2.5" fill="none" stroke="#fff" stroke-width="2" stroke-dasharray="1.6 1"/></svg></div>
  <h3>Es simplemente el texto de</h3>
  <p>Lorem Ipsum is simply dummy text of the printing and typesetting industry. deen the industry's...</p>
</div>
<section class="abs what">
  <h2>WHAT WE DO?</h2>
  <p>Es simplemente el texto de relleno de las imprentas y archivos de texto. Lorem Ipsum ha sido el texto de relleno estándar de las...</p>
</section>
<div class="abs service" style="left:72px">
  <div class="photo" role="img" aria-label="City towers by a marina at sunset" style="background:linear-gradient(#b07a4c,#5a3a2a 60%,#2a1e1c)"></div>
  <h4>Es simplemente el texto de</h4>
  <p>Es simplemente el texto de relleno de las imprentas y archivos de texto.</p>
</div>
<div class="abs service" style="left:256px">
  <div class="photo" role="img" aria-label="Business meeting around an office table" style="background:linear-gradient(135deg,#dfe6ee,#8a9bb0 55%,#2c3a52)"></div>
  <h4>Es simplemente el texto de</h4>
  <p>Es simplemente el texto de relleno de las imprentas y archivos de texto.</p>
</div>
<div class="abs service" style="left:440px">
  <div class="photo" role="img" aria-label="Hands typing on a laptop keyboard holding a pen" style="background:linear-gradient(160deg,#fbfbfb,#e6dcd4 55%,#b9a79a)"></div>
  <h4>Es simplemente el texto de</h4>
  <p>Es simplemente el texto de relleno de las imprentas y archivos de texto.</p>
</div>
<div class="abs service" style="left:624px">
  <div class="photo" role="img" aria-label="Two colleagues reviewing documents together" style="background:linear-gradient(135deg,#f2f2f2,#9fb0c8 50%,#3c5a8a)"></div>
  <h4>Es simplemente el texto de</h4>
  <p>Es simplemente el texto de relleno de las imprentas y archivos de texto.</p>
</div>
<section class="abs partners">
  <div class="partner" style="left:94px">Tallowby</div>
  <div class="partner" style="left:200px"><i></i>Kestrin</div>
  <div class="partner" style="left:340px"><i></i>Orvane Labs</div>
  <div class="partner" style="left:443px"><i style="border-radius:50%"></i>Mirel Studio</div>
  <div class="partner" style="left:580px"><i></i>Quillmark</div>
  <div class="partner" style="left:689px"><i style="border-radius:50%"></i>Dovecrest</div>
</section>
<footer class="abs footer">
  <div class="col" style="left:83px;width:230px">
    <h5>About Us</h5>
    <p>Lorem Ipsum es simplemente el texto de relleno de las imprentas y archivos de texto. Lorem Ipsum ha sido el texto de relleno estándar de las industrias desde el año 1500, cuando un impresor (N. del T. persona que se dedica a la imprenta) desconocido usó una galería de textos y los mezcló de tal manera...</p>
  </div>
  <div class="col" style="left:380px">
    <h5>Welcome</h5>
    <a href="#">About Us</a><a href="#">Services</a><a href="#">solutions</a><a href="#">Carriers</a><a href="#">Clients</a><a href="#">Testimonials</a><a href="#">Contact Us</a>
  </div>
  <div class="col" style="left:521px">
    <h5>Information</h5>
    <a href="#">Privacy Policy</a><a href="#">Terms &amp; Conditions</a><a href="#">Sitemap</a>
  </div>
  <div class="col" style="left:671px">
    <h5>Follow Us</h5>
    <div class="social"><span></span>: Pagewall</div>
    <div class="social"><span></span>Chirpline</div>
    <div class="social"><span></span>: Plusring</div>
    <div class="social"><span></span>: Linkwork</div>
  </div>
</footer>
<div class="abs bottom">© 2015. Fernhold Capital. All rights reserved.</div>
</body>
</html>
```